Larkmoor Leisure Group (LLG)

We need a business card design for Larkmoor Leisure Group. Modern and sleek looking, with all critical information. Open to single or double sided designs, if double sided info needs to be all on one side. The main Logo is Larkmoor Leisure group and must be on the card. The other three logos are for the brands that fall under the group, they might be good on the back.

Industry/Entity Type

Business

```html
<!DOCTYPE html>
<html lang="en">
<head>
<meta charset="utf-8">
<title>Larkmoor Leisure Group – Business Card</title>
<link rel="stylesheet" href="https://fonts.googleapis.com/css2?family=Montserrat:wght@400;500;600;700&family=Exo+2:wght@700&display=swap">
<style>
  :root {
    --brand-blue: #2457a0;
    --brand-green: #8db33a;
    --ink: #222222;
    --paper: #ffffff;
    --backdrop: #dcdcdc;
    --divider: #b9b9b9;
  }
  * { box-sizing: border-box; margin: 0; padding: 0; }
  html, body { width: 1200px; height: 852px; overflow: hidden; }
  body {
    background: var(--backdrop);
    font-family: "Montserrat", Arial, sans-serif;
    position: relative;
  }
  .card {
    position: absolute;
    top: 275px;
    width: 530px;
    height: 302px;
    border-radius: 22px;
    overflow: hidden;
    background: var(--paper);
    box-shadow: 0 6px 18px rgba(0,0,0,.18);
  }
  .card--front { left: 45px; }
  .card--back { left: 625px; }

  /* Front */
  .front__main {
    position: absolute; inset: 0 0 auto 0; height: 200px;
    background: var(--brand-blue);
    display: flex; flex-direction: column; align-items: center; justify-content: center;
    color: var(--paper);
  }
  .mark-square {
    width: 46px; height: 46px; background: var(--paper); margin-bottom: 14px;
  }
  .wordmark { text-align: center; font-weight: 600; }
  .wordmark__name { font-size: 22px; letter-spacing: .5px; text-transform: uppercase; }
  .wordmark__group {
    display: flex; align-items: center; gap: 12px; justify-content: center;
    font-size: 15px; letter-spacing: 9px; text-transform: uppercase; margin-top: 4px;
  }
  .wordmark__rule { width: 68px; height: 2px; background: currentColor; }

  .front__brands {
    position: absolute; top: 200px; left: 0; right: 0; height: 62px;
    display: flex; align-items: center; justify-content: space-evenly;
  }
  .brand-name {
    font-weight: 700; font-size: 17px; color: var(--brand-blue);
  }
  .brand-divider { width: 1px; height: 34px; background: var(--divider); }

  .front__footer {
    position: absolute; bottom: 0; left: 0; right: 0; height: 40px;
    background: var(--brand-blue); color: var(--paper);
    display: flex; align-items: center; justify-content: center;
    font-size: 13px; letter-spacing: .5px;
  }

  /* Back */
  .back__logo {
    position: absolute; top: 34px; right: 40px; width: 210px;
    display: flex; flex-direction: column; align-items: center;
    color: var(--brand-blue);
  }
  .back__logo .mark-square { background: var(--brand-blue); width: 56px; height: 56px; }
  .back__logo .wordmark__name { font-size: 17px; }
  .back__logo .wordmark__group { font-size: 13px; letter-spacing: 8px; }
  .back__logo .wordmark__rule { width: 52px; }

  .person { position: absolute; left: 38px; top: 140px; }
  .person__name {
    font-family: "Exo 2", "Montserrat", sans-serif; font-weight: 700;
    font-size: 24px; color: var(--brand-blue);
  }
  .person__title { font-size: 14px; color: var(--ink); margin-top: 2px; }

  .contact { position: absolute; left: 38px; bottom: 26px; list-style: none; color: var(--ink); font-size: 15px; }
  .contact li { display: flex; align-items: center; gap: 10px; line-height: 23px; }
  .contact svg { width: 13px; height: 13px; fill: var(--brand-blue); flex: none; }
  .contact .no-icon { padding-left: 0; }
  .highlight { color: var(--brand-blue); }
</style>
</head>
<body>

<section class="card card--front" aria-label="Card front">
  <div class="front__main">
    <div class="mark-square"></div>
    <div class="wordmark">
      <div class="wordmark__name">Larkmoor Leisure</div>
      <div class="wordmark__group"><span class="wordmark__rule"></span>Group<span class="wordmark__rule"></span></div>
    </div>
  </div>
  <div class="front__brands">
    <span class="brand-name">MoorTickets</span>
    <span class="brand-divider"></span>
    <span class="brand-name">Boxseat Hospitality</span>
    <span class="brand-divider"></span>
    <span class="brand-name">seatgate</span>
  </div>
  <div class="front__footer">www.larkmoorleisuregroup.com</div>
</section>

<section class="card card--back" aria-label="Card back">
  <div class="back__logo">
    <div class="mark-square"></div>
    <div class="wordmark">
      <div class="wordmark__name">Larkmoor Leisure</div>
      <div class="wordmark__group"><span class="wordmark__rule"></span>Group<span class="wordmark__rule"></span></div>
    </div>
  </div>

  <div class="person">
    <div class="person__name">John Doe Smith</div>
    <div class="person__title">Managing Director</div>
  </div>

  <ul class="contact">
    <li>
      <svg viewBox="0 0 16 16" aria-hidden="true"><path d="M3.5 1l3 3-1.8 1.8a10 10 0 0 0 5.5 5.5L12 9.5l3 3-2 2.2C7 15 1 9 1.3 3z"/></svg>
      555.555.5555
    </li>
    <li>
      <svg viewBox="0 0 16 16" aria-hidden="true"><path d="M1 3h14v10H1z M1 3l7 6 7-6" stroke="#fff" stroke-width="1.2"/></svg>
      johndoe@yourwebsite.com
    </li>
    <li>
      <svg viewBox="0 0 16 16" aria-hidden="true"><circle cx="8" cy="8" r="7"/><path d="M1 8h14M8 1c-3 4-3 10 0 14M8 1c3 4 3 10 0 14" stroke="#fff" stroke-width="1" fill="none"/></svg>
      <span>www.<span class="highlight">yourwebsite</span>.com</span>
    </li>
    <li class="no-icon">234 Anywhere St., Any Town, US 123456</li>
  </ul>
</section>

</body>
</html>
```